Price Package PDF - 2 page PDF of stylized price packages for property management firm

Looking for a 2 x A4 page PDF for our two price packages.
I would like this to be in similar style to our website www.harbourlanerentals.com.au
I have attached an example. But would like mine to be a little more stylish and modern, preferably using design similar to our website.
Words and images also attached

Target Market(s)

investment property owners, male and female, aged 30-60

Industry/Entity Type

Real Estate

Font styles to use
Sans Serif

Requirements
Must have
• split two packages onto seperate A4 pages (See example file attached)
• Contact info:
• Website: www.harbourlanerentals.com.au
• email: info@harbourlanerentals.com.au
• Phone: Tom Radley 0417 562 903, Larisa Okonjo 0409 317 648
• Office Address: Suite 7, 12-14 Wattle Parade, Curl Curl NSW 2096
Nice to have
• I would like to use any of the pictures provided or images of modern residential property interior or of Sydney's Northern Beaches.

```html
<!DOCTYPE html>
<html lang="en">
<head>
<meta charset="utf-8">
<title>Harbour Lane Rentals – All Inclusive Package</title>
<link href="https://fonts.googleapis.com/css2?family=Mulish:wght@400;600;700&display=swap" rel="stylesheet">
<style>
:root{
  --bg:#e9eaeb;
  --paper:#ffffff;
  --ink:#1f1c1d;
  --orange:#e8761a;
  --panel-dark:#231f20;
  --panel-mid:#4b4748;
  --list-bg:#ebebeb;
  --footer:#0b0b0c;
  --white:#ffffff;
}
*{margin:0;padding:0;box-sizing:border-box}
html,body{width:1200px;height:1000px;overflow:hidden;background:var(--bg);font-family:"Mulish",sans-serif;color:var(--ink)}
.flyer{position:absolute;left:278px;top:45px;width:644px;height:910px;background:var(--paper)}
.hero{position:absolute;left:0;top:0;width:644px;height:333px;
  background:linear-gradient(180deg,#3f8fb4 0%,#7fb3c8 28%,#6d7a78 50%,#3e4d3a 75%,#2c3a2a 100%)}
.hero-rule{position:absolute;left:0;top:334px;width:644px;height:4px;background:var(--panel-dark)}
.brand{position:absolute;left:31px;top:64px;color:var(--white);font-weight:600;font-size:29px;letter-spacing:.2px;display:flex;align-items:center;gap:10px}
.brand-mark{width:12px;height:12px;background:var(--white)}
.hero-title{position:absolute;left:32px;top:274px;color:var(--white);font-weight:600;font-size:25px;line-height:23px;text-transform:uppercase}
.includes{position:absolute;left:30px;top:366px;width:289px;height:407px;background:var(--list-bg)}
.panel-head{height:35px;padding:7px 9px;font-size:17px;font-weight:600;color:var(--white)}
.includes .panel-head{background:var(--panel-dark)}
.feature-list{list-style:none;padding:8px 8px 0 8px}
.feature-list li{position:relative;padding-left:11px;font-size:13.5px;line-height:17.8px}
.feature-list li::before,.price-row::before{content:"";position:absolute;left:0;top:5px;width:6px;height:6px;background:var(--orange)}
.pricing{position:absolute;left:346px;top:366px;width:259px;height:232px;background:var(--panel-dark)}
.pricing .panel-head{background:var(--orange)}
.price-row{position:relative;font-size:13.5px;line-height:19px;color:var(--white);padding:1px 6px 0 19px}
.price-row::before{left:7px;top:6px}
.price-row.mid{background:var(--panel-mid)}
.price-row.rate{padding:7px 6px 2px 19px;line-height:20px}
.price-row.rate::before{display:none}
.rate-figure{color:var(--orange);font-size:17px}
.wharf-photo{position:absolute;left:346px;top:607px;width:259px;height:166px;
  background:linear-gradient(170deg,#0e4f86 0%,#3d86bd 45%,#9cc3de 62%,#2e3236 80%,#4a4f55 100%)}
.footer{position:absolute;left:0;top:808px;width:644px;height:102px;background:var(--footer);color:var(--white);font-size:12px}
.contacts{position:absolute;left:60px;top:18px;line-height:21px}
.contacts .name{color:var(--orange)}
.web{position:absolute;left:380px;top:18px;line-height:21px}
.web div{display:flex;align-items:center;gap:6px}
.social{position:absolute;left:300px;top:70px;display:flex;gap:12px}
.social span{width:15px;height:15px;border-radius:3px;background:var(--orange)}
</style>
</head>
<body>
<div class="flyer">
  <div class="hero" role="img" aria-label="Photo of modern terraced townhouses with balconies and lush landscaped gardens under a blue sky"></div>
  <div class="brand"><span>HARBOUR LANE RENTALS</span></div>
  <h1 class="hero-title">All Inclusive<br>Package:</h1>
  <div class="hero-rule"></div>

  <section class="includes">
    <div class="panel-head">Includes:</div>
    <ul class="feature-list">
      <li>Securing Tenant</li>
      <li>Reference/Database Checking</li>
      <li>Lease Preparation and Signing</li>
      <li>Direct Debit rent collection</li>
      <li>Zero arrears policy management</li>
      <li>Payment of Rates and levies</li>
      <li>Insurance management</li>
      <li>Coordination or all repairs and maintenance</li>
      <li>Regular rent reviews and renewals</li>
      <li>Detailed ingoing, ongoing and outgoing inspections with photos and videos viewable through your personal Landlord portal</li>
      <li>Bond management &nbsp;lodging and refunding</li>
      <li>Electronic monthly and EOFY statements</li>
      <li>Annual scheduled maintenance report</li>
      <li>Regulation/compliance management</li>
      <li>Tribunal Representation</li>
    </ul>
  </section>

  <section class="pricing">
    <div class="panel-head">All Inclusive Package:</div>
    <div class="price-row rate mid">Management Rate: <span class="rate-figure">10% +</span> GST of rental income</div>
    <div class="price-row">Letting Fee: No Charge</div>
    <div class="price-row mid">Advertising: No Charge</div>
    <div class="price-row">Professional Photography: $199 (inc GST) 4 x Photos</div>
    <div class="price-row mid">Statements: No Charge</div>
    <div class="price-row">Lease Preparation: No Charge</div>
    <div class="price-row mid" style="padding-bottom:4px">Renewal Fees: No Charge</div>
  </section>

  <div class="wharf-photo" role="img" aria-label="Photo of a harbour wharf building with rooftop lettering against a deep blue sky"></div>

  <footer class="footer">
    <div class="contacts">
      <div><span class="name">Tom Radley</span> 0417 562 903 | <span class="name">Larisa Okonjo</span> 0409 317 648</div>
      <div>Suite 7, 12-14 Wattle Parade, Curl Curl NSW 2096</div>
    </div>
    <div class="web">
      <div><svg width="12" height="9" viewBox="0 0 12 9"><rect x=".5" y=".5" width="11" height="8" fill="none" stroke="#e8761a"/><path d="M.5 .5 6 5l5.5-4.5" fill="none" stroke="#e8761a"/></svg>info@harbourlanerentals.com.au</div>
      <div><svg width="11" height="11" viewBox="0 0 11 11"><circle cx="5.5" cy="5.5" r="5" fill="none" stroke="#e8761a"/><ellipse cx="5.5" cy="5.5" rx="2.2" ry="5" fill="none" stroke="#e8761a"/><path d="M.5 5.5h10" stroke="#e8761a"/></svg>www.harbourlanerentals.com.au</div>
    </div>
    <div class="social"><span></span><span></span></div>
  </footer>
</div>
</body>
</html>
```